Book cover design about quality management systems

Book cover design that I can display in my website for ore orders
The book is about helping organisations to fully integrate their Quality management systems rather than having a quality system which sits off to the side and adds extra work.
It is aimed at organisations leaders
It is about leaders taking ownership and leading the decision and design of the quality management system and therefore being able to delegate more effectively.

Target Market(s)

CEO of government funded organisations

Industry/Entity Type

Management

Font styles to use
Sans Serif

Colors

Designer to choose colors to be used in the design.

Requirements
Must have
• Ability to be used on website
• Title of the book
• Anchor lantern harvest
• Strap line - Letting Quality Lead the Way
Nice to have
• Not too fussy
• Not a black cover
• Deep Yellow in the design if possible
Should not have
• Anything too feminine

```html
<!DOCTYPE html>
<html lang="en">
<head>
<meta charset="utf-8">
<title>Anchor Lantern Harvest – Book Cover</title>
<link rel="stylesheet" href="https://fonts.googleapis.com/css2?family=Jost:ital,wght@0,300;0,700;1,200;1,300&family=Oswald:wght@500;600&display=swap">
<style>
  :root {
    --deep-yellow: #fdaa27;
    --navy: #1f2d5e;
    --white: #ffffff;
  }
  html, body {
    margin: 0;
    padding: 0;
    width: 927px;
    height: 1200px;
    overflow: hidden;
    background: var(--deep-yellow);
  }
  .cover {
    display: block;
    width: 927px;
    height: 1200px;
  }
  .cover__background { fill: var(--deep-yellow); }
  .cover__corner { fill: var(--navy); }
  .cover__frame { fill: none; stroke: var(--navy); stroke-width: 1.5; }
  .cover__bracket { fill: none; stroke: var(--white); stroke-width: 1.6; }
  .title { fill: var(--white); }
  .title__line--bold {
    font-family: "Jost", "Futura", sans-serif;
    font-weight: 700;
    font-size: 184px;
  }
  .title__line--light {
    font-family: "Jost", "Futura", sans-serif;
    font-weight: 300;
    font-style: italic;
    font-size: 170px;
  }
  .title__line--condensed {
    font-family: "Oswald", "Arial Narrow", sans-serif;
    font-weight: 600;
    font-size: 172px;
  }
  .strapline {
    fill: var(--navy);
    font-family: "Oswald", "Arial Narrow", sans-serif;
    font-weight: 600;
    font-size: 50px;
  }
  .byline__label {
    fill: var(--white);
    font-family: "Oswald", "Arial Narrow", sans-serif;
    font-weight: 500;
    font-size: 34px;
  }
  .byline__author {
    fill: var(--white);
    font-family: "Jost", "Futura", sans-serif;
    font-weight: 300;
    font-size: 29px;
  }
</style>
</head>
<body>
<svg class="cover" viewBox="0 0 927 1200" xmlns="http://www.w3.org/2000/svg" role="img" aria-label="Anchor Lantern Harvest – Letting Quality Lead the Way, written by Miriam Holloway">
  <rect class="cover__background" x="0" y="0" width="927" height="1200"/>

  <polygon class="cover__corner cover__corner--top-left" points="0,0 212,0 0,341"/>
  <polygon class="cover__corner cover__corner--bottom-right" points="927,773 927,1200 664,1200"/>

  <rect class="cover__frame" x="55" y="55" width="818" height="1090"/>

  <polyline class="cover__bracket cover__bracket--top-left" points="371,147 161,147 161,326"/>
  <polyline class="cover__bracket cover__bracket--bottom-right" points="765,439 765,621 557,621"/>

  <g class="title">
    <text class="title__line title__line--bold" x="182" y="298" textLength="560" lengthAdjust="spacingAndGlyphs">ANCHOR</text>
    <text class="title__line title__line--light" x="172" y="439" textLength="586" lengthAdjust="spacingAndGlyphs">LANTERN</text>
    <text class="title__line title__line--condensed" x="182" y="598" textLength="560" lengthAdjust="spacingAndGlyphs">HARVEST</text>
  </g>

  <text class="strapline" x="176" y="700" textLength="589" lengthAdjust="spacingAndGlyphs">Letting Quality Lead the Way</text>

  <g class="byline">
    <text class="byline__label" x="388" y="1048" textLength="152" lengthAdjust="spacingAndGlyphs">WRITTEN BY</text>
    <text class="byline__author" x="215" y="1093" textLength="502" lengthAdjust="spacing">MIRIAM HOLLOWAY</text>
  </g>
</svg>
</body>
</html>
```